Business Card Design Project

Hi,
This is a simple contest. The logo for the back of the card is deigned. See attached files. The front of the card must have :

Directors Name: Tobias
Mob:
e-mail:
Postal Address:
Web Page Adress:

It may also add words: "Leaders in Construction Project Management Services"

Target Market(s)

Business & Home owners alike

Industry/Entity Type

Business

Requirements
Must have
• See details above and logo attached
Should not have
• Images other than logo

```html
<!DOCTYPE html>
<html lang="en">
<head>
<meta charset="utf-8">
<title>Keystone Build Group – Business Cards</title>
<link rel="stylesheet" href="https://fonts.googleapis.com/css2?family=Archivo:wght@700&family=Marcellus&display=swap">
<style>
  :root {
    --backdrop: #2b2b2b;
    --card-light: #1c9fd6;
    --card-mid: #127bb0;
    --card-dark: #0a4d72;
    --ink: #ffffff;
    --ink-muted: #b9dcef;
    --ink-label: #8cc3e0;
  }
  * { margin: 0; padding: 0; box-sizing: border-box; }
  html, body { width: 1200px; height: 900px; overflow: hidden; }
  body { background: var(--backdrop); position: relative; }

  .card {
    position: absolute;
    width: 640px;
    height: 366px;
    background: radial-gradient(ellipse at 50% 55%, var(--card-light) 0%, var(--card-mid) 38%, var(--card-dark) 100%);
    box-shadow: 0 10px 30px rgba(0,0,0,0.55);
    color: var(--ink);
  }
  .card--contact { left: 40px; top: 70px; }
  .card--brand { left: 520px; top: 470px; }

  .brand { display: flex; align-items: center; }
  .brand__square { background: var(--ink); flex: none; }
  .brand__name {
    font-family: "Archivo", Arial, sans-serif;
    font-weight: 700;
    color: var(--ink);
    line-height: 1;
    text-transform: uppercase;
  }
  .brand__name span { display: block; }

  /* contact card */
  .card--contact .brand { position: absolute; left: 56px; top: 168px; gap: 14px; }
  .card--contact .brand__square { width: 40px; height: 40px; }
  .card--contact .brand__name span:first-child { font-size: 32px; letter-spacing: 0.5px; }
  .card--contact .brand__name span:last-child { font-size: 13px; letter-spacing: 4px; margin-top: 4px; }

  .divider {
    position: absolute;
    left: 340px; top: 110px;
    width: 2px; height: 170px;
    background: var(--ink);
  }
  .contact {
    position: absolute;
    left: 362px; top: 112px;
    font-family: "Marcellus", Georgia, serif;
  }
  .contact__name { font-size: 19px; color: var(--ink-muted); letter-spacing: 1px; text-transform: uppercase; line-height: 1.1; }
  .contact__role { font-size: 21px; color: var(--ink); letter-spacing: 1px; text-transform: uppercase; line-height: 1.1; margin-bottom: 18px; }
  .contact__list { list-style: none; font-size: 15px; line-height: 1.45; letter-spacing: 0.5px; }
  .contact__list li { display: flex; }
  .contact__label { color: var(--ink-label); width: 92px; text-transform: uppercase; }
  .contact__value { color: var(--ink); text-transform: uppercase; }

  /* brand card */
  .card--brand .brand { position: absolute; left: 72px; top: 128px; gap: 22px; }
  .card--brand .brand__square { width: 72px; height: 72px; }
  .card--brand .brand__name span:first-child { font-size: 60px; letter-spacing: 1px; }
  .card--brand .brand__name span:last-child { font-size: 24px; letter-spacing: 7px; margin-top: 6px; }
  .tagline {
    position: absolute;
    left: 0; right: 0; top: 292px;
    text-align: center;
    font-family: "Marcellus", Georgia, serif;
    font-size: 17px;
    color: var(--ink);
  }
</style>
</head>
<body>
  <section class="card card--contact">
    <div class="brand">
      <div class="brand__square"></div>
      <div class="brand__name"><span>Keystone</span><span>Build Group</span></div>
    </div>
    <div class="divider"></div>
    <div class="contact">
      <p class="contact__name">Tobias</p>
      <p class="contact__role">Director</p>
      <ul class="contact__list">
        <li><span class="contact__label">Mobile :</span><span class="contact__value">123 555 0142</span></li>
        <li><span class="contact__label">Email :</span><span class="contact__value">tobias@mail.com</span></li>
        <li><span class="contact__label">Address :</span><span class="contact__value">Harwood, WI 5420</span></li>
        <li><span class="contact__label">Website :</span><span class="contact__value">www.kbgroup.com</span></li>
      </ul>
    </div>
  </section>

  <section class="card card--brand">
    <div class="brand">
      <div class="brand__square"></div>
      <div class="brand__name"><span>Keystone</span><span>Build Group</span></div>
    </div>
    <p class="tagline">"Leaders in Construction Project Management Services"</p>
  </section>
</body>
</html>
```